Classic Minimalistic Business Card

Design a classic, minimalistic Business Card. Please find inspiration in the attached Classic Minimalistic examples. My information:
Name: Glen Whitacre
Company: Whitacre Capital
Logo: WC
Address: 1800 N Corliss Ave, Suite 420 | Geneva, IL 60187
Phone: 630-555-0172
Email: glenwhitacre@tvm.example
Slogan: Unlocking the Power of Capital

Feel free to leave out any of the information above except my name.

I have selected Double-sided, but I am also open to Single-sided

Target Market(s)

22-70. income greater than 150k/year

Industry/Entity Type

Finance

Contact Information for Business Card

See Project Description

Requirements
Must have
• Ivory or "antiqued" background similar to the reference pictures

```html
<!DOCTYPE html>
<html lang="en">
<head>
<meta charset="utf-8">
<title>Whitacre Capital Business Card</title>
<link rel="stylesheet" href="https://fonts.googleapis.com/css2?family=Abril+Fatface&family=Inter:ital,wght@0,400;0,600;1,400&display=swap">
<style>
  :root {
    --backdrop: #e6dbd1;
    --card-dark: #4a4b4e;
    --card-ivory: #f2eee5;
    --ink-light: #efe9dc;
    --ink-dark: #3b3c3f;
    --ink-muted: #56575a;
    --mark-fill: #6a6a6d;
  }
  * { margin: 0; padding: 0; box-sizing: border-box; }
  html, body { width: 881px; height: 1200px; overflow: hidden; }
  body {
    background: var(--backdrop);
    font-family: "Inter", Arial, sans-serif;
    display: flex;
    flex-direction: column;
    align-items: center;
    justify-content: center;
    gap: 100px;
  }
  .card {
    position: relative;
    width: 700px;
    height: 400px;
    box-shadow: 0 6px 18px rgba(60, 45, 35, 0.18);
  }
  .card--front {
    background: var(--card-dark);
    color: var(--ink-light);
    display: flex;
    flex-direction: column;
    align-items: center;
    justify-content: center;
    text-align: center;
  }
  .person-name {
    font-family: "Abril Fatface", Georgia, serif;
    font-weight: 400;
    font-size: 46px;
    letter-spacing: 0.5px;
    margin-bottom: 46px;
  }
  .contact-line {
    font-size: 16px;
    letter-spacing: 2.5px;
    line-height: 1.6;
  }
  .card--back {
    background: var(--card-ivory);
    color: var(--ink-dark);
  }
  .slogan {
    position: absolute;
    top: 40px;
    left: 40px;
    font-size: 16px;
    line-height: 1.25;
    color: var(--ink-muted);
  }
  .slogan-lead { font-weight: 600; display: block; }
  .slogan-rest { font-style: italic; display: block; }
  .company-name {
    position: absolute;
    top: 178px;
    left: 0;
    right: 0;
    text-align: center;
    font-family: "Abril Fatface", Georgia, serif;
    font-weight: 400;
    font-size: 46px;
    letter-spacing: 0.5px;
  }
  .company-mark {
    position: absolute;
    top: 150px;
    right: 40px;
    width: 64px;
    height: 64px;
    border-radius: 50%;
    background: var(--mark-fill);
  }
  .address {
    position: absolute;
    bottom: 42px;
    left: 40px;
    font-size: 16px;
    letter-spacing: 2px;
    color: var(--ink-muted);
  }
</style>
</head>
<body>
  <section class="card card--front">
    <h1 class="person-name">Glen Whitacre</h1>
    <p class="contact-line">630-555-0172</p>
    <p class="contact-line">glenwhitacre@tvm.example</p>
  </section>

  <section class="card card--back">
    <p class="slogan">
      <span class="slogan-lead">Unlocking</span>
      <span class="slogan-rest">the Power of Capital</span>
    </p>
    <div class="company-mark" aria-hidden="true"></div>
    <h2 class="company-name">Whitacre Capital</h2>
    <p class="address">1800 N Corliss Ave, Suite 420 | Geneva, IL 60187</p>
  </section>
</body>
</html>
```